Business Card and Word .doc header and footer required

I need a business card designed for my cybersecurity consulting company. Also required, is a header and footer to be ued for my word documents.
Attached is the Logo design, font and rgb used.

Industry/Entity Type

Cyber Security Consulting

Contact Information for Business Card

Name, Phone, email, website

Colors
0054AA
0677BA
7BADD7
CADEEF
E8F1F8

Requirements
Must have
• Sleek, modern

```html
<!DOCTYPE html>
<html lang="en">
<head>
<meta charset="utf-8">
<title>Halvern Cyber – Business Card</title>
<link rel="stylesheet" href="https://fonts.googleapis.com/css2?family=Montserrat:wght@400;500;600;700&display=swap">
<style>
  :root {
    --page-bg: #ffffff;
    --card-bg: #3a3a3b;
    --card-bg-dark: #333334;
    --deco-dark: #1f2022;
    --text-white: #ffffff;
    --text-soft: #d9d9d9;
    --brand-blue: #0677BA;
    --brand-blue-bright: #1596d6;
    --divider: #6a6a6a;
  }
  * { box-sizing: border-box; margin: 0; padding: 0; }
  html, body {
    width: 1004px; height: 1200px; overflow: hidden;
    background: var(--page-bg);
    font-family: "Montserrat", sans-serif;
  }
  .sheet { position: relative; width: 1004px; height: 1200px; }
  .card {
    position: absolute; top: 470px;
    width: 432px; height: 259px; overflow: hidden;
    background: linear-gradient(135deg, var(--card-bg) 0%, var(--card-bg-dark) 100%);
    color: var(--text-white);
  }
  .card--front { left: 55px; }
  .card--back { left: 517px; }

  /* Brand block */
  .brand { position: absolute; text-align: center; }
  .brand__mark {
    display: block; margin: 0 auto 18px;
    width: 72px; height: 72px; border-radius: 50%;
    background: var(--text-white);
  }
  .brand__name {
    font-weight: 600; font-size: 20px; letter-spacing: 0.2px;
    color: var(--brand-blue-bright); white-space: nowrap; line-height: 1;
  }
  .brand__tagline {
    margin-top: 9px; font-size: 7px; letter-spacing: 3.6px;
    color: var(--text-soft); white-space: nowrap;
  }
  .card--front .brand { left: 0; width: 234px; top: 58px; }

  .divider {
    position: absolute; left: 221px; top: 76px;
    width: 1px; height: 114px; background: var(--divider);
  }

  .contact { position: absolute; left: 254px; top: 67px; }
  .contact__name { font-weight: 600; font-size: 16px; letter-spacing: 0.4px; line-height: 1; }
  .contact__role { margin-top: 6px; font-size: 9px; color: var(--text-soft); }
  .contact__address { margin-top: 13px; font-size: 9.5px; font-weight: 500; line-height: 12px; }
  .contact__row {
    display: flex; align-items: center; gap: 7px;
    margin-top: 11px; font-size: 9.5px; font-weight: 500;
  }
  .contact__row + .contact__row { margin-top: 5px; }
  .icon-badge {
    width: 16px; height: 16px; border-radius: 50%;
    background: var(--brand-blue-bright);
    display: flex; align-items: center; justify-content: center;
  }

  .footer-rule { position: absolute; left: 0; top: 225px; width: 432px; height: 14px; }
  .website {
    position: absolute; top: 225px; left: 0; width: 432px;
    text-align: center; font-size: 10px; font-weight: 500; line-height: 14px;
  }

  /* Back */
  .deco-disc {
    position: absolute; left: -88px; top: 0;
    width: 260px; height: 260px; border-radius: 50%;
    background: var(--deco-dark);
  }
  .card--back .brand { right: 23px; top: 181px; }
  .card--back .brand__name { font-size: 26px; }
  .card--back .brand__tagline { font-size: 7.5px; letter-spacing: 3.4px; margin-top: 10px; }
</style>
</head>
<body>
<main class="sheet">

  <section class="card card--front" aria-label="Business card front">
    <div class="brand">
      <span class="brand__mark"></span>
      <p class="brand__name">Halvern Cyber</p>
      <p class="brand__tagline">CONSULTING COMPANY</p>
    </div>

    <div class="divider"></div>

    <div class="contact">
      <p class="contact__name">RAFAEL ODUYA</p>
      <p class="contact__role">Graphic Designer</p>
      <p class="contact__address">48 Quarry Lane, Suite 3<br>Ashford, NY 10412</p>
      <p class="contact__row">
        <span class="icon-badge">
          <svg width="9" height="9" viewBox="0 0 24 24" aria-hidden="true"><path fill="#fff" d="M6.6 10.8a15 15 0 0 0 6.6 6.6l2.2-2.2c.3-.3.7-.4 1-.2 1.1.4 2.3.6 3.6.6.6 0 1 .4 1 1V20c0 .6-.4 1-1 1A17 17 0 0 1 3 4c0-.6.4-1 1-1h3.5c.6 0 1 .4 1 1 0 1.3.2 2.5.6 3.6.1.3 0 .7-.2 1z"/></svg>
        </span>
        555 . 204 7718
      </p>
      <p class="contact__row">
        <span class="icon-badge">
          <svg width="9" height="9" viewBox="0 0 24 24" aria-hidden="true"><rect x="2" y="5" width="20" height="14" rx="1.5" fill="none" stroke="#fff" stroke-width="2"/><path d="M3 6l9 7 9-7" fill="none" stroke="#fff" stroke-width="2"/></svg>
        </span>
        hello@halverncyber.com
      </p>
    </div>

    <svg class="footer-rule" viewBox="0 0 432 14" aria-hidden="true">
      <line x1="20" y1="7" x2="146" y2="7" stroke="#0677BA" stroke-width="1"/>
      <line x1="284" y1="7" x2="410" y2="7" stroke="#0677BA" stroke-width="1"/>
      <circle cx="20" cy="7" r="2.5" fill="#1596d6"/>
      <circle cx="410" cy="7" r="2.5" fill="#1596d6"/>
    </svg>
    <p class="website">www.halverncyber.com</p>
  </section>

  <section class="card card--back" aria-label="Business card back">
    <span class="deco-disc"></span>
    <div class="brand">
      <p class="brand__name">Halvern Cyber</p>
      <p class="brand__tagline">CONSULTING COMPANY</p>
    </div>
  </section>

</main>
</body>
</html>
```